Business card design needed for Pollen Bakes

We need a new business card designed for our business. We create complete DIY cake kits to be delivered Australia Wide.

I would like our logo used (see attached).

Industry/Entity Type

Business

Contact Information for Business Card

Pollen Bakes - Complete DIY Cake Kits
www.pollenbakes.com.au
0472 315 904
sales@pollenbakes.com.au
www.facebook.com/pollenbakes1

Requirements
Must have
• logo

```html
<!DOCTYPE html>
<html lang="en">
<head>
<meta charset="utf-8">
<title>Pollen Bakes – Business Card</title>
<link rel="stylesheet" href="https://fonts.googleapis.com/css2?family=Arvo:wght@700&family=Lobster&family=Questrial&display=swap">
<style>
  :root {
    --page-bg: #ece7e3;
    --card-pink: #d95aac;
    --card-pink-light: #e27cc0;
    --ribbon-pink: #e2338a;
    --ribbon-shadow: #a81e63;
    --title-ink: #2f2a2c;
    --text-white: #ffffff;
    --logo-red: #c21f3a;
    --art-hair: #8a5a36;
    --art-skin: #f3d2b5;
    --art-frosting: #f27cc0;
  }
  * { box-sizing: border-box; margin: 0; padding: 0; }
  html, body {
    width: 1200px; height: 794px; overflow: hidden;
    background: var(--page-bg);
  }
  .canvas {
    position: relative; width: 1200px; height: 794px;
  }
  .card {
    position: absolute; left: 80px; top: 100px;
    width: 1040px; height: 594px;
    background: var(--card-pink);
    overflow: hidden;
    box-shadow: 0 6px 18px rgba(0,0,0,.18);
  }
  .card-band {
    position: absolute; left: 0; right: 0; top: 250px; bottom: 0;
    background: var(--card-pink-light);
  }
  .brand-title {
    position: absolute; left: 60px; top: 150px;
    font-family: "Arvo", serif; font-weight: 700; font-size: 66px;
    color: var(--text-white);
    -webkit-text-stroke: 3px var(--title-ink);
    paint-order: stroke fill;
    text-shadow: 4px 5px 0 var(--title-ink);
    letter-spacing: 1px;
  }
  .tagline {
    position: absolute; left: 74px; top: 238px;
    width: 440px; height: 48px; border-radius: 10px;
    background: var(--ribbon-pink);
    box-shadow: 0 6px 0 var(--ribbon-shadow);
    font-family: "Lobster", cursive; font-size: 30px;
    color: var(--text-white); text-align: center; line-height: 48px;
  }
  .contact {
    position: absolute; left: 60px; top: 310px; width: 500px;
    font-family: "Questrial", sans-serif; font-size: 31px;
    color: var(--text-white); text-align: center; line-height: 40px;
  }
  .social {
    position: absolute; left: 70px; bottom: 36px;
    display: flex; align-items: center; gap: 8px;
    font-family: "Questrial", sans-serif; font-size: 23px;
    color: var(--text-white);
  }
  .social-mark {
    width: 26px; height: 26px; border-radius: 4px;
    background: var(--text-white);
  }
  .mascot-art {
    position: absolute; left: 690px; top: 30px;
    width: 300px; height: 360px; border-radius: 40px 40px 20px 20px;
    background: linear-gradient(180deg, var(--art-hair) 0%, var(--art-skin) 45%, var(--art-frosting) 100%);
  }
  .logo-name {
    position: absolute; left: 640px; top: 410px; width: 380px;
    font-family: "Questrial", sans-serif; font-size: 58px;
    color: var(--logo-red); text-align: center;
  }
</style>
</head>
<body>
  <main class="canvas">
    <section class="card">
      <div class="card-band"></div>

      <h1 class="brand-title">Pollen Bakes</h1>
      <p class="tagline">Complete DIY Cake Kits</p>

      <address class="contact">
        www.pollenbakes.com.au<br>
        0472 315 904<br>
        sales@pollenbakes.com.au
      </address>

      <div class="social">
        <span class="social-mark"></span>
        <span>fb.com/pollenbakes1</span>
      </div>

      <div class="mascot-art" role="img" aria-label="Illustrated mascot of a curly-haired baker holding a piping bag and a pink-frosted cupcake"></div>
      <p class="logo-name">Pollen Bakes</p>
    </section>
  </main>
</body>
</html>
```